Business Card - Ridge Wellness

Please use the logo / design elements and font to design a business card that is eye catching and informative. If using "Direct Primary Care" logo element, you don't have to spell it out in the text.

Dr. Calvin Pettrow
Ridge Wellness - Direct Primary Care
4817 Tallow Creek Rd. Suite 305
Fort Smith, AR 72903
Phone: 479-555-0173
RidgeWellnessQX.com

```html
<!DOCTYPE html>
<html lang="en">
<head>
<meta charset="utf-8">
<title>Ridge Wellness – Business Card</title>
<link rel="stylesheet" href="https://fonts.googleapis.com/css2?family=Poppins:wght@500;600;700&family=Roboto:wght@400&display=swap">
<style>
  :root {
    --stage: #2e2e2e;
    --navy: #021135;
    --royal: #1f55d0;
    --sky: #29b6ef;
    --white: #ffffff;
    --ink: #1c1c1c;
    --rule: #7d8290;
  }
  * { box-sizing: border-box; margin: 0; padding: 0; }
  html, body { width: 1200px; height: 694px; overflow: hidden; }
  body {
    background: var(--stage);
    position: relative;
    font-family: "Roboto", Arial, sans-serif;
  }
  .card {
    position: absolute;
    top: 192px;
    width: 540px;
    height: 309px;
    border-radius: 18px;
    overflow: hidden;
  }

  /* Front */
  .card--front { left: 40px; background: var(--navy); }
  .front-brand {
    position: absolute;
    left: 0; right: 0; top: 118px;
    display: flex; align-items: center; justify-content: center; gap: 14px;
  }
  .front-brand .brand-dot {
    width: 22px; height: 22px; border-radius: 50%; background: var(--sky);
  }
  .front-brand .brand-name {
    font-family: "Poppins", Arial, sans-serif;
    font-weight: 600;
    font-size: 50px;
    color: var(--white);
    letter-spacing: -0.5px;
    line-height: 1;
  }
  .front-rule {
    position: absolute; height: 1px; background: var(--white); top: 204px;
  }
  .front-rule--left { left: 72px; width: 120px; }
  .front-rule--right { right: 72px; width: 120px; }

  /* Back */
  .card--back { left: 620px; background: var(--white); }
  .back-brand {
    position: absolute; right: 36px; top: 44px;
    display: flex; align-items: center; gap: 8px;
  }
  .back-brand .brand-dot {
    width: 11px; height: 11px; border-radius: 50%; background: var(--sky);
  }
  .back-brand .brand-name {
    font-family: "Poppins", Arial, sans-serif;
    font-weight: 600;
    font-size: 26px;
    color: var(--navy);
    letter-spacing: -0.3px;
    line-height: 1;
  }
  .back-brand-rule {
    position: absolute; right: 36px; top: 84px; width: 224px; height: 1px; background: var(--navy);
  }
  .holder-name {
    position: absolute; left: 34px; top: 176px;
    font-family: "Poppins", Arial, sans-serif;
    font-weight: 700; font-size: 22px; color: var(--navy);
  }
  .address {
    position: absolute; right: 34px; top: 158px;
    text-align: right; font-size: 14px; line-height: 1.45; color: var(--ink);
  }
  .divider {
    position: absolute; left: 34px; right: 34px; top: 212px; height: 1px; background: var(--rule);
  }
  .contacts {
    position: absolute; left: 34px; top: 224px; list-style: none;
    font-size: 14px; color: var(--ink);
  }
  .contacts li { display: flex; align-items: center; gap: 10px; height: 22px; }
  .contacts svg { width: 14px; height: 14px; flex: none; }
  .color-band {
    position: absolute; left: 0; right: 0; bottom: 0; height: 10px; display: flex;
  }
  .color-band span:nth-child(1) { flex: 40; background: var(--royal); }
  .color-band span:nth-child(2) { flex: 34; background: var(--sky); }
  .color-band span:nth-child(3) { flex: 26; background: var(--navy); }
</style>
</head>
<body>
  <section class="card card--front" aria-label="Card front">
    <div class="front-brand">
      <span class="brand-dot"></span>
      <span class="brand-name">Ridge Wellness</span>
    </div>
    <span class="front-rule front-rule--left"></span>
    <span class="front-rule front-rule--right"></span>
  </section>

  <section class="card card--back" aria-label="Card back">
    <div class="back-brand">
      <span class="brand-dot"></span>
      <span class="brand-name">Ridge Wellness</span>
    </div>
    <span class="back-brand-rule"></span>

    <h1 class="holder-name">Dr. Calvin Pettrow</h1>
    <address class="address">4817 Tallow Creek Rd. Suite 305<br>Fort Smith, AR 72903</address>
    <span class="divider"></span>

    <ul class="contacts">
      <li>
        <svg viewBox="0 0 24 24" aria-hidden="true"><path fill="#1f55d0" d="M6.6 10.8a15.1 15.1 0 0 0 6.6 6.6l2.2-2.2a1 1 0 0 1 1-.25 11.4 11.4 0 0 0 3.6.57 1 1 0 0 1 1 1V20a1 1 0 0 1-1 1A17 17 0 0 1 3 4a1 1 0 0 1 1-1h3.5a1 1 0 0 1 1 1c0 1.25.2 2.45.57 3.57a1 1 0 0 1-.25 1z"/></svg>
        479-555-0173
      </li>
      <li>
        <svg viewBox="0 0 24 24" aria-hidden="true"><circle cx="12" cy="12" r="10" fill="#1f55d0"/><path d="M2 12h20M12 2c3 3 3 17 0 20M12 2c-3 3-3 17 0 20" stroke="#fff" stroke-width="1.5" fill="none"/></svg>
        www.RidgeWellnessQX.com
      </li>
    </ul>

    <div class="color-band"><span></span><span></span><span></span></div>
  </section>
</body>
</html>
```